Brindle's Custom Signs and Woodworking Business Card

I run a small business that does custom woodworking and sign making. I have a logo already that I am very fond of, and would like to continue with the theme of the logo. I'd like a business card that adds onto that theme/design and stands out among typical business cards. As you'll be able to see from the logo, we're a patriotic brand and that is paramount to us.
Contact Information for Business Card
beneath the Brindle's logo, I'd like it to say
"Custom Signs & Woodworking"
Also, I'd like the following information template present on the card, preferably with the logos of instagram and facebook present besides the title.
(Name)                                 (Instragram)
(Email)                                  (Facebook)
(Phone)                                 (Website)
I would like for the name, email, and phone number to be editable so that I can have my employees utilize this card design as well. but for my card, my information is as follows
Dan "Brindle" Korvell, CEO                                           @BrindlesCustoms
Dan@BrindlesCustoms.example                                          Brindle's Customs
(555) 274-6103                                                         BrindlesCustoms.example
As for the back side, either a full american flag, or something that catches the eye, designer's preference I suppose.
Font styles to use
Other font styles liked:
- Funkydori, an adobe typekit font. it is the same as used for the logo. I'm not sure how the whole card will look with that, so if it doesn't look right please use something that complements the script style of the logo

```html
<!DOCTYPE html>
<html lang="en">
<head>
<meta charset="utf-8">
<title>Brindle's Custom Signs &amp; Woodworking – Business Card</title>
<link rel="stylesheet" href="https://fonts.googleapis.com/css2?family=Cormorant+Garamond:ital,wght@0,500;0,600;0,700;1,500&family=Lato:wght@400;700&display=swap">
<style>
  :root {
    --page-bg: #e9e6e1;
    --navy: #131a4a;
    --navy-deep: #0c1036;
    --navy-light: #2a3170;
    --flag-red: #9c1c26;
    --flag-cream: #efe9e4;
    --flag-blush: #e2c9c6;
    --gold: #c7a97c;
    --gold-dim: #a88d66;
    --ink: #2b2b33;
  }
  * { margin: 0; padding: 0; box-sizing: border-box; }
  html, body { width: 1200px; height: 970px; overflow: hidden; }
  body {
    background: var(--page-bg);
    position: relative;
  }
  .business-card {
    position: absolute;
    left: 100px; top: 199px;
    width: 1000px; height: 572px;
    border-radius: 28px;
    overflow: hidden;
    box-shadow: 0 18px 40px rgba(0,0,0,0.18);
  }
  .card-art { position: absolute; inset: 0; width: 100%; height: 100%; display: block; }
  .brand {
    position: absolute;
    left: 50px; top: 200px;
    width: 380px;
    text-align: center;
  }
  .brand-name {
    font-family: "Cormorant Garamond", serif;
    font-weight: 700;
    font-size: 96px;
    line-height: 1;
    color: var(--navy);
  }
  .brand-tagline {
    margin-top: 34px;
    font-family: "Lato", sans-serif;
    font-size: 24px;
    color: var(--ink);
    letter-spacing: 0.2px;
  }
  .holder {
    position: absolute;
    left: 610px; top: 98px;
    font-family: "Cormorant Garamond", serif;
    color: var(--gold);
  }
  .holder-name { font-size: 36px; font-weight: 600; line-height: 1.05; }
  .holder-title { font-size: 26px; font-weight: 500; line-height: 1.1; letter-spacing: 0.5px; }
  .contact-list {
    position: absolute;
    left: 610px; top: 268px;
    list-style: none;
    font-family: "Cormorant Garamond", serif;
    font-size: 25px;
    font-weight: 500;
    color: var(--gold);
  }
  .contact-item { display: flex; align-items: center; height: 35.5px; }
  .contact-item:nth-child(4) { color: var(--gold-dim); }
  .contact-icon { width: 30px; height: 30px; margin-right: 14px; flex: none; }
  .website {
    position: absolute;
    left: 610px; top: 440px;
    font-family: "Cormorant Garamond", serif;
    font-style: italic;
    font-size: 22px;
    letter-spacing: 6px;
    color: var(--gold-dim);
  }
</style>
</head>
<body>
  <section class="business-card" aria-label="Brindle's Custom Signs and Woodworking business card">
    <svg class="card-art" viewBox="0 0 1000 572" preserveAspectRatio="none" aria-hidden="false">
      <defs>
        <linearGradient id="navyPanel" x1="0" y1="0" x2="1" y2="1">
          <stop offset="0" stop-color="#1a2160"/>
          <stop offset="0.55" stop-color="#131a4a"/>
          <stop offset="1" stop-color="#0c1036"/>
        </linearGradient>
        <linearGradient id="flagField" x1="0" y1="0" x2="0.3" y2="1">
          <stop offset="0" stop-color="#d8d3d6"/>
          <stop offset="0.45" stop-color="#efe9e4"/>
          <stop offset="0.8" stop-color="#e2c9c6"/>
          <stop offset="1" stop-color="#d9d2d0"/>
        </linearGradient>
      </defs>
      <rect class="navy-panel" width="1000" height="572" fill="url(#navyPanel)"/>
      <path class="red-edge" d="M0 0 H470 C555 110 580 300 520 420 C490 480 450 530 400 572 H0 Z" fill="#9c1c26"/>
      <path class="flag-panel" role="img" aria-label="Soft waving American flag background with stars and stripes"
            d="M0 0 H460 C540 110 562 300 505 420 C476 478 432 530 378 572 H0 Z" fill="url(#flagField)"/>
    </svg>

    <div class="brand">
      <div class="brand-name">Brindle's</div>
      <div class="brand-tagline">Custom Signs &amp; Woodworking</div>
    </div>

    <div class="holder">
      <div class="holder-name">Dan "Brindle" Korvell</div>
      <div class="holder-title">CEO</div>
    </div>

    <ul class="contact-list">
      <li class="contact-item">
        <svg class="contact-icon" viewBox="0 0 30 30" aria-hidden="true">
          <circle cx="15" cy="15" r="13" fill="none" stroke="currentColor" stroke-width="2"/>
          <path d="M9 12 C9 9 21 9 21 12 L19 13.5 L17 12.5 V11.5 H13 V12.5 L11 13.5 Z M10 15 H20 L21 20 H9 Z" fill="currentColor"/>
        </svg>
        (555) 274-6103
      </li>
      <li class="contact-item">
        <svg class="contact-icon" viewBox="0 0 30 30" aria-hidden="true">
          <circle cx="15" cy="15" r="13" fill="none" stroke="currentColor" stroke-width="2"/>
          <rect x="9" y="10.5" width="12" height="9" fill="currentColor"/>
          <path d="M9 10.5 L15 16 L21 10.5" fill="none" stroke="#131a4a" stroke-width="1.4"/>
        </svg>
        Dan@BrindlesCustoms.example
      </li>
      <li class="contact-item">
        <svg class="contact-icon" viewBox="0 0 30 30" aria-hidden="true">
          <circle cx="15" cy="15" r="13" fill="none" stroke="currentColor" stroke-width="2"/>
        </svg>
        @BrindlesCustoms
      </li>
      <li class="contact-item">
        <svg class="contact-icon" viewBox="0 0 30 30" aria-hidden="true">
          <circle cx="15" cy="15" r="13" fill="none" stroke="currentColor" stroke-width="2"/>
        </svg>
        Brindle's Customs
      </li>
    </ul>

    <div class="website">BrindlesCustoms.example</div>
  </section>
</body>
</html>
```